Free Range Egg Farmer wants a Egg Carton Design

We need a design for Free Range Egg carton. Our company name is "BrookHaven The Craft of Growing"

We run a environmentally friendly farm in Gippsland VIC and we produce Free Range Eggs and Pasture Fed Meats in open pasture.

We also run a farm stay business in a very high energy star rating house.
The farm guest participates in our farm activity such as looking after farm animals, maintaining the vegetable garden, cooking fresh food, Yoga and Meditation.

We would like to see designs with our logo and something alternative rather than a typical free range egg cartons.

The team had a meeting and came up with one idea.
"The meditating hen" with thought bubble which we can change the hen's thought by printing batch.
You could either use this idea or create your own.

I have attached 3 photos close to my image as examples.
I also have attached the typical free range egg cartons as examples.

Sticker size is attached. The sticker fits between the case closure system. So there is no need to make spaces for the closure gaps.
Please place Best Before stamp area at the top right corner of the main (middle) section.
Updates

I have post an update to my brief. Please have a look again. BrookHaven

Industry/Entity Type

Printing

Requirements
Must have
• Company name,
Address,
contact number,
facebook logo,
best before date (space to put the stamp on)
12 Free Range Eggs xxx g
Nutrition info

```html
<!DOCTYPE html>
<html lang="en">
<head>
<meta charset="utf-8">
<title>BrookHaven Free Range Eggs – Carton Label</title>
<link rel="stylesheet" href="https://fonts.googleapis.com/css2?family=Lato:wght@400;700;900&family=Cinzel:wght@500&display=swap">
<style>
  :root {
    --canvas: #a7a9ac;
    --paper: #ffffff;
    --leaf: #a6ce39;
    --brand-red: #e8383d;
    --tag-green: #4d6a2b;
    --egg-blue: #3b3d92;
    --ink: #2f2f2f;
    --alert-red: #e2231a;
    --badge-dark: #1f4a34;
    --burst-light: #ffc20e;
    --burst-deep: #f26522;
    --dash: #8a8a8a;
  }
  * { box-sizing: border-box; margin: 0; padding: 0; }
  html, body { width: 1200px; height: 1000px; overflow: hidden; }
  body { background: var(--canvas); font-family: "Lato", Arial, sans-serif; color: var(--ink); position: relative; }

  .panel { position: absolute; background: var(--paper); border-radius: 22px; overflow: hidden; }
  .panel--lid { left: 193px; top: 143px; width: 815px; height: 153px; }
  .panel--main { left: 190px; top: 308px; width: 817px; height: 383px; background: var(--leaf); }
  .panel--front { left: 190px; top: 704px; width: 817px; height: 153px; }

  .lid-inner { position: absolute; inset: 0; transform: rotate(180deg); }

  .stamp-box { position: absolute; width: 58px; height: 58px; border: 1px dashed var(--dash); }
  .weight-tag { position: absolute; width: 132px; height: 85px; background: var(--leaf); border-radius: 14px;
    color: #fff; font-weight: 700; font-size: 19px; line-height: 22px; text-align: center;
    display: flex; align-items: center; justify-content: center; }

  /* lid */
  .nutrition { position: absolute; left: 28px; top: 20px; font-size: 14px; font-weight: 700; }
  .best-before { position: absolute; left: 28px; top: 114px; font-size: 9px; color: var(--alert-red); }
  .batch-info { position: absolute; left: 578px; top: 42px; font-size: 9.5px; font-weight: 700; line-height: 19px; }
  .batch-info .row { display: flex; }
  .batch-info .label { width: 64px; }
  .batch-info .colon { width: 14px; }

  /* main */
  .main-art { position: absolute; inset: 0; }
  .brand-seal { position: absolute; left: 71px; top: 42px; width: 100px; height: 100px; border-radius: 50%;
    background: var(--badge-dark); color: #fff; font-weight: 700; font-size: 15px;
    display: flex; align-items: center; justify-content: center; }
  .brand-name { position: absolute; left: 0; width: 817px; top: 100px; text-align: center;
    font-family: "Lato", Arial, sans-serif; font-weight: 900; font-size: 86px; color: var(--brand-red); letter-spacing: -1px; }
  .tagline { position: absolute; left: 395px; top: 228px; font-size: 20px; font-weight: 700; color: var(--tag-green); }
  .product-title { position: absolute; left: 0; width: 817px; top: 318px; text-align: center;
    font-family: "Cinzel", Georgia, serif; font-weight: 500; font-size: 40px; color: var(--egg-blue); letter-spacing: 1px; }
  .count-burst { position: absolute; left: 668px; top: 252px; width: 108px; height: 108px; }
  .count-burst .count { position: absolute; inset: 0; text-align: center; padding-top: 14px; font-weight: 700; color: var(--ink); }
  .count-burst .num { font-size: 38px; line-height: 38px; display: block; }
  .count-burst .unit { font-size: 10.5px; line-height: 12px; display: block; color: #fff; }

  /* front */
  .maker { position: absolute; left: 31px; top: 41px; }
  .maker .lead { font-size: 10.5px; font-weight: 700; }
  .maker .name { font-size: 24px; font-weight: 700; margin-top: 3px; }
  .maker .address { font-size: 10px; font-weight: 700; line-height: 12px; margin-top: 3px; }
  .contact { position: absolute; right: 25px; top: 42px; text-align: center; width: 230px; }
  .contact .phone { font-size: 24px; font-weight: 700; display: flex; align-items: center; justify-content: flex-end; gap: 4px; }
  .contact .follow { font-size: 9px; margin-top: 5px; display: flex; align-items: center; justify-content: center; gap: 3px; }
  .contact .social { width: 13px; height: 13px; background: #3b6cb4; display: inline-block; }
  .contact .web { font-size: 13px; margin-top: 5px; }
</style>
</head>
<body>

  <section class="panel panel--lid" aria-label="Carton lid flap">
    <div class="lid-inner">
      <p class="nutrition">Nutrition Facts :</p>
      <p class="best-before">Best before 3months from the date of Manufature</p>
      <div class="stamp-box" style="left:260px; top:47px;"></div>
      <div class="weight-tag" style="left:341px; top:34px;">12 Free<br>Range Eggs<br>xxx g</div>
      <div class="stamp-box" style="left:502px; top:47px;"></div>
      <div class="batch-info">
        <div class="row"><span class="label">Mfg. Lic No.</span><span class="colon">:</span></div>
        <div class="row"><span class="label">Batch No.</span><span class="colon">:</span></div>
        <div class="row"><span class="label">MFG Date</span><span class="colon">:</span></div>
        <div class="row"><span class="label">Net Content</span><span class="colon">:</span><span>12 Free Range Eggs xxx g</span></div>
      </div>
    </div>
  </section>

  <section class="panel panel--main" aria-label="Carton top panel">
    <svg class="main-art" width="817" height="383" viewBox="0 0 817 383">
      <path d="M95 0 C70 90 45 170 70 240 C95 310 140 350 170 383 L690 383 C730 340 760 280 770 200 C780 120 760 60 745 0 Z" fill="var(--paper)"/>
      <g role="img" aria-label="Green brush-stroke circle framing the brand name">
        <circle cx="410" cy="182" r="128" fill="none" stroke="var(--leaf)" stroke-width="16"/>
      </g>
    </svg>
    <div class="brand-seal">BrookHaven</div>
    <div class="brand-name">BrookHaven</div>
    <div class="tagline">The Craft of Growing</div>
    <div class="product-title">Free Range Eggs</div>
    <div class="count-burst">
      <svg width="108" height="108" viewBox="0 0 108 108">
        <defs>
          <radialGradient id="burstFill" cx="50%" cy="40%" r="60%">
            <stop offset="0" stop-color="var(--burst-light)"/>
            <stop offset="1" stop-color="var(--burst-deep)"/>
          </radialGradient>
        </defs>
        <polygon fill="url(#burstFill)" points="54,2 61,17 75,7 77,24 94,20 89,36 105,41 93,53 105,66 89,71 94,88 77,84 75,101 61,91 54,106 47,91 33,101 31,84 14,88 19,71 3,66 15,54 3,41 19,36 14,20 31,24 33,7 47,17"/>
      </svg>
      <div class="count"><span class="num">12</span><span class="unit">Free Range<br>Eggs</span></div>
    </div>
  </section>

  <section class="panel panel--front" aria-label="Carton front flap">
    <div class="maker">
      <p class="lead">Manufactured &amp; Marketed by :</p>
      <p class="name">BrookHaven</p>
      <p class="address">Lot 2418, Pasture Lane, Sector No. 14,<br>Riverton - 3871. AUSTRALIA.</p>
    </div>
    <div class="stamp-box" style="left:258px; top:47px;"></div>
    <div class="weight-tag" style="left:342px; top:34px;">12 Free<br>Range Eggs<br>xxx g</div>
    <div class="stamp-box" style="left:500px; top:47px;"></div>
    <div class="contact">
      <p class="phone">
        <svg width="22" height="24" viewBox="0 0 24 24" aria-hidden="true"><path d="M6.6 10.8c1.4 2.8 3.8 5.1 6.6 6.6l2.2-2.2c.3-.3.7-.4 1-.2 1.1.4 2.3.6 3.6.6.6 0 1 .4 1 1V20c0 .6-.4 1-1 1C10.6 21 3 13.4 3 4c0-.6.4-1 1-1h3.5c.6 0 1 .4 1 1 0 1.3.2 2.5.6 3.6.1.3 0 .7-.2 1z" fill="var(--ink)"/></svg>
        +61 3 5600 4821
      </p>
      <p class="follow">Follow us on <span class="social"></span><span class="social"></span><span class="social"></span></p>
      <p class="web">www.brookhaven.com.au.</p>
    </div>
  </section>

</body>
</html>
```